Sports Performance Lab needs a new website

We need an updated/new website for Vondel Arc Human Performance Lab. We recently moved from Florida to the Chicago area. We perform testing ranging from VO2 Max, Lactate Threshold, Resting Metabolic Rate, Body Composition Testing with the TRU SHELL and Metabolic Efficiency Testing. We also have a mobile lab contained in a 24 foot trailer. We work with athletes, coaches, Fitness Gyms, Pivot Drill Gyms to improve performance and also with people looking to manage or lose weight. Our current site is www.vondelarclab.example. Looking for an improved site, better grahics/photos but also blends into our current logo and graphics on Mobile Lab. Would like a calendar/ appointment page on website

Colors
ec1f27
000000
fbed22

Requirements
Must have
• ability to easily updatae
Nice to have
• appointment calendar

```html
<!DOCTYPE html>
<html lang="en">
<head>
<meta charset="utf-8">
<title>Vondel Arc Human Performance Lab</title>
<link href="https://fonts.googleapis.com/css2?family=Lato:wght@400;700;900&display=swap" rel="stylesheet">
<style>
:root{
  --red:#ec1f27;
  --black:#000000;
  --yellow:#fbed22;
  --ink:#222222;
  --muted:#6b6b6b;
  --dark:#1c1c1c;
  --panel:#2a2a2a;
  --line:#dddddd;
  --white:#ffffff;
}
*{box-sizing:border-box;margin:0;padding:0}
html,body{width:1200px;height:3904px;overflow:hidden}
body{font-family:"Lato",Arial,sans-serif;color:var(--ink);background:var(--white);position:relative}
section,header,footer{position:relative;width:1200px;overflow:hidden}
.notch{position:absolute;left:50%;bottom:-1px;margin-left:-18px;width:0;height:0;border-left:18px solid transparent;border-right:18px solid transparent;border-bottom:18px solid var(--white)}
.notch.down{bottom:auto;top:0;border-bottom:0;border-top:18px solid var(--red)}

/* header */
.site-header{height:160px;background:var(--white)}
.topbar{position:absolute;right:0;top:0;height:40px;width:300px;background:var(--red);color:var(--white);font-weight:700;font-size:20px;display:flex;align-items:center;justify-content:flex-end;padding-right:40px;gap:10px;z-index:2}
.brand{position:absolute;left:40px;top:40px;display:flex;align-items:center;gap:10px}
.brand-mark{width:26px;height:26px;background:var(--red)}
.brand-name{font-weight:900;font-size:30px;line-height:34px;color:var(--black);letter-spacing:1px;white-space:nowrap}
.brand-sub{position:absolute;left:40px;top:80px;font-size:11px;color:var(--muted);letter-spacing:2px;white-space:nowrap}
.socials{position:absolute;left:40px;top:110px;display:flex;gap:8px}
.socials span{width:24px;height:24px;border-radius:50%;background:var(--ink)}
.nav{position:absolute;right:30px;top:40px;height:120px;display:flex;align-items:center}
.nav a{display:block;padding:0 11px;line-height:120px;font-size:13px;font-weight:900;color:var(--ink);text-decoration:none;white-space:nowrap}
.nav a.active{background:var(--yellow);padding:0 16px}

/* hero */
.hero{height:600px}
.hero-photo{position:absolute;inset:0;background:linear-gradient(135deg,#6f7f8c 0%,#45515c 45%,#2b333a 100%)}
.hero-caption{position:absolute;left:0;right:0;bottom:0;height:80px;background:rgba(0,0,0,.55);color:var(--white);font-size:22px;font-weight:700;padding:26px 40px}
.hero-arrow{position:absolute;top:270px;width:40px;height:60px;background:rgba(0,0,0,.45)}
.hero-arrow.l{left:0}.hero-arrow.r{right:0}
.hero-arrow svg{display:block;margin:18px auto}

/* welcome */
.welcome{height:440px;padding-top:48px}
.welcome-text{position:absolute;left:40px;top:48px;width:680px}
.section-h{font-size:30px;font-weight:900;color:var(--black)}
.section-h small{font-size:16px;font-weight:700;margin-left:4px}
.welcome-text p{margin-top:20px;font-size:15px;line-height:25px;color:var(--muted)}
.btn-red{display:inline-block;margin-top:24px;background:var(--red);color:var(--white);font-size:13px;font-weight:900;padding:10px 22px;border-radius:3px}
.calendar{position:absolute;left:770px;top:48px;width:390px}
.cal-bar{margin-top:14px;height:44px;background:var(--red);color:var(--white);display:flex;align-items:center;justify-content:space-between;padding:0 16px;font-weight:900;font-size:17px}
.cal-grid{display:grid;grid-template-columns:repeat(7,1fr);gap:4px;margin-top:4px}
.cal-grid div{height:36px;display:flex;align-items:center;justify-content:center;font-size:14px;font-weight:700;background:#e6e6e6;color:#555}
.cal-grid .hd{background:#444;color:var(--white)}
.cal-grid .we{background:var(--yellow);color:var(--ink)}
.cal-grid .hd.we{background:#666;color:var(--white)}
.cal-grid .em{background:#f2f2f2}
.cal-grid .sel{background:var(--red);color:var(--white)}

/* services */
.services{height:660px}
.services-bg{position:absolute;inset:0;background:linear-gradient(180deg,#2e2e2e,#151515)}
.services .title{position:relative;text-align:center;color:var(--white);font-size:30px;font-weight:900;padding-top:60px}
.cards{position:absolute;left:60px;top:140px;display:flex;gap:30px}
.card{width:247px;height:430px;background:var(--white);padding:14px;text-align:center}
.card-photo{height:180px;background:linear-gradient(135deg,#9aa3ab,#5a646c)}
.card h3{margin-top:22px;font-size:18px;font-weight:900}
.card p{margin-top:12px;font-size:13px;line-height:21px;color:var(--muted)}
.btn-line{display:inline-block;margin-top:18px;border:1px solid var(--red);color:var(--red);font-size:12px;font-weight:700;padding:7px 20px}

/* testing */
.testing{height:620px}
.testing .title{text-align:center;font-size:30px;font-weight:900;padding-top:40px;height:100px}
.tiles{display:grid;grid-template-columns:repeat(4,300px);grid-auto-rows:260px}
.tile{position:relative}
.tile .ph{position:absolute;inset:0}
.tile .lbl{position:absolute;left:0;right:0;bottom:0;height:40px;background:rgba(0,0,0,.6);color:var(--white);font-size:14px;font-weight:700;text-align:center;line-height:40px}

/* cta */
.cta{height:320px}
.cta-bg{position:absolute;inset:0;background:linear-gradient(120deg,#3a3a3a,#1a1a1a 60%,#2a2620)}
.cta-text{position:relative;text-align:center;color:var(--white);font-size:30px;line-height:44px;padding-top:90px}
.btn-yellow{display:inline-block;background:var(--yellow);color:var(--black);font-weight:900;font-size:18px;line-height:24px;padding:12px 28px;margin-top:22px;border-radius:3px}

/* reviews */
.reviews{height:500px}
.reviews .title{text-align:center;font-size:30px;font-weight:900;padding-top:40px}
.quote{position:relative;width:980px;margin:30px auto 0;text-align:center;font-size:15px;line-height:25px;color:var(--muted);font-style:italic}
.qmark{position:absolute;top:-10px;font-size:70px;font-weight:900;color:var(--ink);font-style:normal;line-height:1}
.qmark.l{left:-50px}.qmark.r{right:-50px}
.reviewer{text-align:center;margin-top:18px;font-weight:700;font-size:14px;font-style:italic}
.avatars{display:flex;justify-content:center;gap:22px;margin-top:44px}
.avatars span{width:84px;height:84px;background:linear-gradient(180deg,#bdbdbd,#8d8d8d);border:3px solid var(--white);outline:1px solid var(--line)}
.avatars span.on{border-color:var(--red);outline:none}

/* contact */
.contact{height:440px;background:var(--dark);color:var(--white)}
.contact .title{text-align:center;font-size:30px;font-weight:900;padding-top:30px}
.cols{position:absolute;left:100px;top:110px;display:flex;gap:90px}
.col h4{font-size:20px;font-weight:700;margin-bottom:14px}
.form{width:300px}
.field{height:30px;background:var(--panel);border:1px solid #3a3a3a;margin-bottom:8px;font-size:12px;color:#999;padding:7px 10px}
.field.msg{height:90px}
.send{display:inline-block;background:var(--yellow);color:var(--black);font-weight:900;font-size:13px;padding:8px 20px;margin-top:6px}
.map{width:300px;height:240px;background:linear-gradient(135deg,#c9d3dc,#9fb0bf)}
.find{width:260px;font-size:13px;line-height:22px;color:#cfcfcf}
.find .row{display:flex;gap:10px;align-items:flex-start;margin-bottom:12px}
.find svg{flex:none;margin-top:3px}
.find .socials{position:static;margin-top:8px}
.find .socials span{background:var(--red)}

/* newsletter */
.newsletter{height:110px;background:var(--red);color:var(--white)}
.nl-inner{position:absolute;left:100px;top:27px;display:flex;align-items:center;gap:18px}
.nl-icon{width:56px;height:56px;border-radius:50%;border:2px solid var(--white);display:flex;align-items:center;justify-content:center}
.nl-title{font-size:28px;font-weight:900;width:400px}
.nl-input{width:380px;height:44px;background:var(--white);color:#999;font-size:14px;padding:12px 14px}
.nl-btn{height:44px;background:var(--yellow);color:var(--black);font-weight:900;font-size:18px;padding:10px 34px}
.site-footer{height:54px;background:var(--black);color:#aaa;font-size:12px;text-align:center;line-height:54px}
</style>
</head>
<body>

<header class="site-header">
  <div class="brand"><span class="brand-mark"></span><span class="brand-name">VONDEL ARC</span></div>
  <div class="brand-sub">HUMAN PERFORMANCE LAB</div>
  <div class="socials"><span></span><span></span><span></span><span></span></div>
  <div class="topbar">
    <svg width="18" height="18" viewBox="0 0 24 24"><path fill="#fff" d="M6.6 10.8a15 15 0 006.6 6.6l2.2-2.2c.3-.3.7-.4 1-.2 1.1.4 2.3.6 3.6.6.6 0 1 .4 1 1V20c0 .6-.4 1-1 1A17 17 0 013 4c0-.6.4-1 1-1h3.5c.6 0 1 .4 1 1 0 1.3.2 2.5.6 3.6.1.3 0 .7-.2 1z"/></svg>
    555-014-2290
  </div>
  <nav class="nav">
    <a class="active">HOME</a><a>ABOUT</a><a>FITNESS TESTS</a><a>TRU SHELL</a><a>COACHES CORNER</a><a>CORPORATE WELLNESS</a><a>CONTACT</a>
  </nav>
</header>

<section class="hero">
  <div class="hero-photo" role="img" aria-label="Athlete running a treadmill test while lab staff monitor results"></div>
  <div class="hero-arrow l"><svg width="14" height="24" viewBox="0 0 14 24"><path d="M12 2L2 12l10 10" stroke="#fff" stroke-width="3" fill="none"/></svg></div>
  <div class="hero-arrow r"><svg width="14" height="24" viewBox="0 0 14 24"><path d="M2 2l10 10L2 22" stroke="#fff" stroke-width="3" fill="none"/></svg></div>
  <div class="hero-caption">Vondel Arc is a mobile Sports and Human Performance Testing Center owned and operated by Marek Halloway</div>
</section>

<section class="welcome">
  <div class="welcome-text">
    <h2 class="section-h">Welcome To Vondel Arc <small>Human Performance Lab</small></h2>
    <p>Our lab measures what matters for athletes, coaches and anyone working toward a healthier weight. Every session starts with a short consultation so we understand your goals, your training history and the results you want to reach. From there we select the right tests, run them with calibrated equipment and explain every number in plain language. You leave with a clear report and practical zones you can use in training the very next day. Our mobile lab brings the same testing to your gym, team or workplace anywhere in the region.</p>
    <span class="btn-red">READ MORE</span>
  </div>
  <div class="calendar">
    <h2 class="section-h">Appointment Calendar</h2>
    <div class="cal-bar">
      <svg width="10" height="14" viewBox="0 0 10 14"><path d="M8 1L2 7l6 6" stroke="#fff" stroke-width="2.5" fill="none"/></svg>
      JULY 2016
      <svg width="10" height="14" viewBox="0 0 10 14"><path d="M2 1l6 6-6 6" stroke="#fff" stroke-width="2.5" fill="none"/></svg>
    </div>
    <div class="cal-grid">
      <div class="hd">Mon</div><div class="hd">Tue</div><div class="hd">Wed</div><div class="hd">Thu</div><div class="hd">Fri</div><div class="hd we">Sat</div><div class="hd we">Sun</div>
      <div class="em"></div><div class="em"></div><div class="em"></div><div class="em"></div><div>01</div><div class="we">02</div><div class="we">03</div>
      <div>04</div><div>05</div><div>06</div><div>07</div><div>08</div><div class="we">09</div><div class="we">10</div>
      <div>11</div><div>12</div><div>13</div><div>14</div><div>15</div><div class="we">16</div><div class="we">17</div>
      <div>18</div><div>19</div><div>20</div><div>21</div><div>22</div><div class="sel">23</div><div class="we">24</div>
      <div>25</div><div>26</div><div>27</div><div>28</div><div>29</div><div class="we">30</div><div class="we">31</div>
    </div>
  </div>
  <div class="notch" style="border-bottom-color:#2e2e2e"></div>
</section>

<section class="services">
  <div class="services-bg" role="img" aria-label="Darkened photo of the testing lab interior"></div>
  <div class="notch down"></div>
  <h2 class="title">Our Services</h2>
  <div class="cards">
    <div class="card"><div class="card-photo" role="img" aria-label="Athlete during a fitness test"></div><h3>Fitness Tests</h3><p>Measure aerobic capacity, thresholds and metabolism with lab grade testing built for every level of athlete.</p><span class="btn-line">Read More</span></div>
    <div class="card"><div class="card-photo" role="img" aria-label="Body composition testing chamber"></div><h3>TRU SHELL</h3><p>Accurate body composition using air displacement, showing lean mass and fat mass in a few minutes.</p><span class="btn-line">Read More</span></div>
    <div class="card"><div class="card-photo" role="img" aria-label="Coach reviewing athlete data"></div><h3>Coaches Corner</h3><p>Tools and data that help coaches plan smarter training blocks and track team progress all season.</p><span class="btn-line">Read More</span></div>
    <div class="card"><div class="card-photo" role="img" aria-label="Employees in a workplace wellness session"></div><h3>Corporate Wellness</h3><p>On site testing and wellness programs that help employees move more, feel better and stay healthy.</p><span class="btn-line">Read More</span></div>
  </div>
  <div class="notch"></div>
</section>

<section class="testing">
  <h2 class="title">We Perform Testing Ranging From</h2>
  <div class="tiles">
    <div class="tile"><div class="ph" role="img" aria-label="Resting metabolic rate test" style="background:linear-gradient(135deg,#7c8a96,#3f4a53)"></div><div class="lbl">Resting Metabolic Rate</div></div>
    <div class="tile"><div class="ph" role="img" aria-label="Body composition test" style="background:linear-gradient(135deg,#8f8a80,#4d4a44)"></div><div class="lbl">TRU SHELL Testing</div></div>
    <div class="tile"><div class="ph" role="img" aria-label="VO2 test on a treadmill" style="background:linear-gradient(135deg,#a49a8c,#5c554c)"></div><div class="lbl">VO2 Testing</div></div>
    <div class="tile"><div class="ph" role="img" aria-label="Metabolic efficiency test on a bike" style="background:linear-gradient(135deg,#86929c,#414b54)"></div><div class="lbl">Metabolic Efficiency Testing</div></div>
    <div class="tile"><div class="ph" role="img" aria-label="VO2 max test" style="background:linear-gradient(135deg,#6f7a84,#353d44)"></div><div class="lbl">VO2 Max</div></div>
    <div class="tile"><div class="ph" role="img" aria-label="Lactate threshold test" style="background:linear-gradient(135deg,#959a9e,#51565a)"></div><div class="lbl">Lactate Threshold</div></div>
    <div class="tile"><div class="ph" role="img" aria-label="Resting metabolic rate measurement" style="background:linear-gradient(135deg,#7e8791,#3c434a)"></div><div class="lbl">Resting Metabolic Rate</div></div>
    <div class="tile"><div class="ph" role="img" aria-label="Athlete on treadmill with mask" style="background:linear-gradient(135deg,#9c9287,#554d45)"></div><div class="lbl">VO2 Max</div></div>
  </div>
</section>

<section class="cta">
  <div class="cta-bg" role="img" aria-label="Side of the mobile testing trailer"></div>
  <div class="notch down" style="border-top-color:#4a4a4a"></div>
  <p class="cta-text">Contact us to bring the Vondel Arc Human Performance Lab to<br>your business or employee wellness event<br><span class="btn-yellow">Contact Us Today</span></p>
  <div class="notch"></div>
</section>

<section class="reviews">
  <h2 class="title">Customer Reviews</h2>
  <div class="quote">
    <span class="qmark l">&ldquo;</span>
    Testing with the team changed how I train. My zones finally make sense, my long runs feel easier and I took four minutes off my marathon time this spring. The report was clear and the staff explained every number patiently.
    <span class="qmark r">&rdquo;</span>
  </div>
  <div class="reviewer">- Jordan Ellery</div>
  <div class="avatars" role="img" aria-label="Row of customer portrait thumbnails">
    <span></span><span class="on"></span><span></span><span></span><span></span><span></span><span></span><span></span><span></span><span></span>
  </div>
  <div class="notch" style="border-bottom-color:var(--dark)"></div>
</section>

<section class="contact">
  <h2 class="title">Contact Us</h2>
  <div class="cols">
    <div class="col form">
      <h4>Quick Inquiry</h4>
      <div class="field">Name</div><div class="field">Email</div><div class="field">Subject</div><div class="field msg">Message</div>
      <span class="send">Send</span>
    </div>
    <div class="col">
      <h4>Location Map</h4>
      <div class="map" role="img" aria-label="Street map showing the lab location"></div>
    </div>
    <div class="col find">
      <h4 style="color:#fff">Find Us</h4>
      <div class="row"><svg width="12" height="16" viewBox="0 0 12 16"><path fill="#ec1f27" d="M6 0a6 6 0 00-6 6c0 4.5 6 10 6 10s6-5.5 6-10a6 6 0 00-6-6zm0 8.5A2.5 2.5 0 116 3.5a2.5 2.5 0 010 5z"/></svg><span>2140 Larkspur Avenue, Suite 8, Naperville, IL 60540</span></div>
      <div class="row"><svg width="14" height="14" viewBox="0 0 24 24"><path fill="#ec1f27" d="M6.6 10.8a15 15 0 006.6 6.6l2.2-2.2c.3-.3.7-.4 1-.2 1.1.4 2.3.6 3.6.6.6 0 1 .4 1 1V20c0 .6-.4 1-1 1A17 17 0 013 4c0-.6.4-1 1-1h3.5c.6 0 1 .4 1 1 0 1.3.2 2.5.6 3.6.1.3 0 .7-.2 1z"/></svg><span>555-014-2290</span></div>
      <div class="row"><svg width="14" height="14" viewBox="0 0 24 24"><rect x="3" y="7" width="18" height="12" fill="#ec1f27"/><rect x="7" y="3" width="10" height="5" fill="#ec1f27"/></svg><span>555-014-2291</span></div>
      <div class="row"><svg width="14" height="12" viewBox="0 0 16 12"><rect width="16" height="12" fill="#ec1f27"/><path d="M0 0l8 7 8-7" stroke="#1c1c1c" stroke-width="1.5" fill="none"/></svg><span>info@vondelarclab.example</span></div>
      <div class="socials"><span></span><span></span><span></span><span></span></div>
    </div>
  </div>
</section>

<section class="newsletter">
  <div class="nl-inner">
    <div class="nl-icon"><svg width="26" height="20" viewBox="0 0 16 12"><rect x=".75" y=".75" width="14.5" height="10.5" fill="none" stroke="#fff" stroke-width="1.5"/><path d="M1 1l7 6 7-6" stroke="#fff" stroke-width="1.5" fill="none"/></svg></div>
    <div class="nl-title">Sign Up For Newsletter</div>
    <div class="nl-input">Enter your email here</div>
    <div class="nl-btn">Subscribe</div>
  </div>
</section>

<footer class="site-footer">Copyright 2016 Vondel Arc Human Performance Lab | All rights reserved</footer>

</body>
</html>
```